CuraNex System Web Page Design

This project is to design 6 pages of a web based medical system for clinics, hospitals, drugs suppliers, general items suppliers, insurance company, laboratories and patients (basically all parties which could be involved in).We want the designs of the browser, button, icon and layout are based on Vex, which is user friendly, looks professional, simple and neat but with powerful functions. We have uploaded few pictures of another system, please do not copy its design because this is not what we are looking for, the pictures are for you to know the elements should be included in our pages. CuraNex web-base system, design 6 pages1. Login PageShould include the following elements-company id with input field-login id with input field-password with input field2. Main Page (Navigation page)Should include the following elements-Appointment-Consultation-Patient-Drugs inventory -General supplies inventory -Laboratory-Suppliers-Insurance-Reports 3. Appointment PageShould include all the the elements in the respective pictures plus the followings-Daily View, Weekly View, Monthly View buttons4. Consultation PageShould include all the the elements in the respective picture5. Patient Page5.1 General information Should include all the the elements in the respective picture5.2 medical history/lab reportsShould include all the the elements in the respective picture plus the followings-Notify patient button-Share report button.
Updated on 28 Nov:
Please stop using Ward Keystone in your designs which is not the name of our system. We have just rename our system to CuraNex, please take note.
We need the system to look professional not playful, do not use too many colors and playful icons.
professional users

```html
<!DOCTYPE html>
<html lang="en">
<head>
<meta charset="utf-8">
<title>CuraNex – Main Navigation</title>
<link href="https://fonts.googleapis.com/css2?family=Open+Sans:wght@400;600&display=swap" rel="stylesheet">
<style>
:root{
  --white:#ffffff;
  --navy:#1b3553;
  --text-dark:#2d3e50;
  --tile:rgba(56,176,186,0.88);
  --side-1:#1d9fa8;
  --side-2:#22adb6;
  --side-3:#25b9c3;
  --side-4:#22c3ce;
  --side-5:#1dcfdb;
  --side-6:#17dbe8;
}
*{box-sizing:border-box;margin:0;padding:0}
html,body{width:1200px;height:674px;overflow:hidden}
body{font-family:"Open Sans",Arial,sans-serif;position:relative;background:#cfe0ea}
.hero-photo{position:absolute;left:0;top:45px;width:1200px;height:629px;
  background:radial-gradient(ellipse at 50% 45%,#c7dce6 0%,#aecbd8 45%,#8fb6c6 100%)}
.topbar{position:absolute;left:0;top:0;width:1200px;height:45px;background:var(--white);
  display:flex;align-items:center;font-size:11.5px;color:#3a4350}
.info{position:absolute;display:flex;align-items:center;gap:7px;top:12px}
.info .dot{width:21px;height:21px;border-radius:50%;background:var(--navy);display:flex;align-items:center;justify-content:center}
.user{position:absolute;left:845px;top:11px;display:flex;align-items:center;gap:7px}
.avatar{width:22px;height:22px;border-radius:50%;background:#7b7f84}
.lang{position:absolute;left:988px;top:16px;display:flex;align-items:center;gap:8px}
.flag{width:18px;height:12px;background:#2b4c8c;border:1px solid #d23a3a}
.brand{position:absolute;left:0;width:1200px;top:78px;text-align:center;font-size:30px;
  font-weight:400;letter-spacing:2px;color:var(--white)}
.grid{position:absolute;left:307px;top:306px;display:grid;grid-template-columns:repeat(4,135px);
  grid-auto-rows:124px;gap:16px 15px}
.tile{background:var(--tile);border-radius:6px;display:flex;flex-direction:column;align-items:center;
  justify-content:center;color:var(--white);font-size:13.5px;text-align:center;line-height:1.35;gap:8px}
.tile svg{width:36px;height:36px}
.sidebar{position:absolute;left:1126px;top:140px;width:74px}
.side-item{height:73.6px;display:flex;flex-direction:column;align-items:center;justify-content:center;
  color:var(--white);font-size:10px;text-transform:uppercase;text-align:center;line-height:1.3;gap:5px}
.side-item svg{width:28px;height:28px}
.footer{position:absolute;left:0;width:1200px;top:619px;text-align:center;font-size:13px;color:var(--text-dark)}
</style>
</head>
<body>
<div class="hero-photo" role="img" aria-label="Background photo of a doctor with a child patient and parent"></div>

<header class="topbar">
  <div class="info" style="left:173px">
    <span class="dot"><svg width="11" height="11" viewBox="0 0 24 24"><path fill="#fff" d="M6.6 10.8a15 15 0 0 0 6.6 6.6l2.2-2.2a1 1 0 0 1 1-.25 11.4 11.4 0 0 0 3.6.57 1 1 0 0 1 1 1V20a1 1 0 0 1-1 1A17 17 0 0 1 3 4a1 1 0 0 1 1-1h3.5a1 1 0 0 1 1 1c0 1.25.2 2.45.57 3.57a1 1 0 0 1-.25 1z"/></svg></span>
    000-0000-0000
  </div>
  <div class="info" style="left:308px">
    <span class="dot"><svg width="11" height="11" viewBox="0 0 24 24"><path fill="#fff" d="M12 2a7 7 0 0 0-7 7c0 5 7 13 7 13s7-8 7-13a7 7 0 0 0-7-7zm0 9.5A2.5 2.5 0 1 1 12 6.5a2.5 2.5 0 0 1 0 5z"/></svg></span>
    25A, Nemo enim ipsam voluptatem
  </div>
  <div class="info" style="left:549px">
    <span class="dot"><svg width="12" height="12" viewBox="0 0 24 24" fill="none" stroke="#fff" stroke-width="2.5"><circle cx="12" cy="12" r="8"/><path d="M12 7v5l3 2"/></svg></span>
    Mon - Sat: 8:00A.M. - 7:00P.M.
  </div>
  <div class="user"><span class="avatar" role="img" aria-label="User profile photo"></span>Liam Hartwell
    <svg width="9" height="6" viewBox="0 0 10 6" fill="none" stroke="#555" stroke-width="1.4"><path d="M1 1l4 4 4-4"/></svg></div>
  <div class="lang"><span class="flag" role="img" aria-label="English language flag"></span>
    <svg width="9" height="6" viewBox="0 0 10 6" fill="none" stroke="#555" stroke-width="1.4"><path d="M1 1l4 4 4-4"/></svg></div>
</header>

<div class="brand">CuraNex</div>

<nav class="grid">
  <a class="tile"><svg viewBox="0 0 36 36" fill="none" stroke="#fff" stroke-width="2"><rect x="5" y="7" width="26" height="24" rx="2"/><path d="M5 13h26M11 4v6M25 4v6M10 18h3M16 18h3M22 18h3M10 24h3M16 24h3M20 27l8-8"/></svg>Appointment</a>
  <a class="tile"><svg viewBox="0 0 36 36" fill="#fff"><circle cx="18" cy="16" r="10"/><path d="M6 16a12 12 0 0 1 24 0" fill="none" stroke="#fff" stroke-width="2"/><rect x="4" y="14" width="4" height="7" rx="1"/><rect x="28" y="14" width="4" height="7" rx="1"/><path d="M9 30a9 5 0 0 1 18 0z"/></svg>Consultation</a>
  <a class="tile"><svg viewBox="0 0 36 36" fill="#fff"><path d="M17 2h2v4h4v2h-4v4h-2V8h-4V6h4z"/><rect x="3" y="14" width="3" height="20"/><circle cx="11" cy="20" r="3"/><rect x="6" y="24" width="27" height="4"/><rect x="16" y="18" width="17" height="6" rx="1"/><rect x="30" y="28" width="3" height="6"/></svg>Patient</a>
  <a class="tile"><svg viewBox="0 0 36 36" fill="#fff"><rect x="4" y="12" width="18" height="12" rx="6" transform="rotate(-45 13 18)"/><circle cx="24" cy="23" r="8"/><path d="M24 15v16" stroke="rgba(56,176,186,1)" stroke-width="2"/></svg>Drugs Inventory</a>
  <a class="tile"><svg viewBox="0 0 36 36" fill="none" stroke="#fff" stroke-width="2.2"><rect x="5" y="12" width="26" height="19" rx="3"/><path d="M13 12V8h10v4M5 19h26M15 19v4h6v-4M18 2v3M10 4l2 3M26 4l-2 3"/></svg>General Suppliers<br>Inventory</a>
  <a class="tile"><svg viewBox="0 0 36 36" fill="#fff"><rect x="14" y="3" width="5" height="14" rx="1" transform="rotate(-20 16 10)"/><rect x="9" y="28" width="20" height="4"/><path d="M12 28a9 9 0 0 1 14-9" fill="none" stroke="#fff" stroke-width="2.5"/><rect x="17" y="20" width="8" height="3"/></svg>Laboratory</a>
  <a class="tile"><svg viewBox="0 0 36 36" fill="#fff"><circle cx="10" cy="6" r="3"/><path d="M7 11h6l2 8h3v3h-5l-2-4-2 6 3 7H9l-3-7 1-13z"/><rect x="19" y="13" width="14" height="9"/><rect x="19" y="23" width="14" height="7"/><circle cx="22" cy="33" r="2"/><circle cx="30" cy="33" r="2"/></svg>Suppliers</a>
  <a class="tile"><svg viewBox="0 0 36 36" fill="#fff"><path d="M18 20l-7-7a4 4 0 0 1 7-5 4 4 0 0 1 7 5z"/><path d="M3 12c2 0 3 2 3 4v6l7 7v5H9v-3L3 24zM33 12c-2 0-3 2-3 4v6l-7 7v5h4v-3l6-7z"/></svg>Insurance</a>
</nav>

<aside class="sidebar">
  <div class="side-item" style="background:var(--side-1)"><svg viewBox="0 0 28 28" fill="none" stroke="#fff" stroke-width="1.6"><path d="M6 2h12l5 5v19H6z"/><rect x="9" y="8" width="10" height="7"/><path d="M9 18h10M9 21h7"/></svg>Reports</div>
  <div class="side-item" style="background:var(--side-2)"><svg viewBox="0 0 28 28" fill="none" stroke="#fff" stroke-width="1.6"><path d="M6 2h12l5 5v19H6z"/><path d="M14 9v10M9 14h10"/></svg>Request<br>Form</div>
  <div class="side-item" style="background:var(--side-3)"><svg viewBox="0 0 28 28" fill="none" stroke="#fff" stroke-width="1.6"><rect x="3" y="5" width="22" height="20" rx="2"/><path d="M3 10h22M8 2v5M20 2v5M7 14h2M13 14h2M19 14h2M7 19h2M13 19h2M19 19h2"/></svg>Doctors<br>Timetable</div>
  <div class="side-item" style="background:var(--side-4)"><svg viewBox="0 0 28 28" fill="none" stroke="#fff" stroke-width="1.6"><rect x="5" y="2" width="18" height="24" rx="2"/><rect x="8" y="5" width="12" height="5"/><path d="M8 13h3v3H8zM13 13h3v3h-3zM18 13h2v3h-2zM8 18h3v3H8zM13 18h3v3h-3zM18 18h2v5h-2z"/></svg>Calculator</div>
  <div class="side-item" style="background:var(--side-5)"><svg viewBox="0 0 28 28" fill="none" stroke="#fff" stroke-width="1.6"><path d="M6 4h4l2 5-3 2a14 14 0 0 0 7 7l2-3 5 2v4a2 2 0 0 1-2 2A19 19 0 0 1 4 6a2 2 0 0 1 2-2z"/><path d="M17 3a8 8 0 0 1 8 8M17 7a4 4 0 0 1 4 4"/></svg>Emergency<br>Case</div>
  <div class="side-item" style="background:var(--side-6)"><svg viewBox="0 0 28 28" fill="none" stroke="#fff" stroke-width="1.6"><path d="M14 2a8 8 0 0 0-8 8c0 6 8 16 8 16s8-10 8-16a8 8 0 0 0-8-8z"/><circle cx="14" cy="10" r="3"/></svg>Location</div>
</aside>

<footer class="footer">© Copyright information here</footer>
</body>
</html>
```